Corvenly Postbox Website Concept (3 Pages)

We're looking to take this website: http://www.corvenlypostbox.example, and redesign it to be more e-commerce oriented. We'd also like to incorporate a seperate page for a blog. The key target is retail customers.
We're looking for a design that has e-commerce like: http://www.trindomart.example/mailboxes.htm?r=1, but still has the homey, stylish feel of: https://quillharbox.example/.
+Pages To Be Designed:
-Home Page
-Product Page
-Main Shopping Page
+Colors:
Attached in files is the color, please make the 'marine' the primary color.
+Home Page
-Incorporate the information from the Residential and Commercial pages on the original website
-Seal or Banner that says Veteran Owned Business
-Seal or Banner that show we are eco-friendly
-Social media link
-DO NOT worry about a gallery page from the original website
-Testimonial section
Target Market(s)
Retail customers
Industry/Entity Type
Sales
Number of Pages Required
3 page
Requirements
Must have
- +Pages To Be Designed:
- -Home Page
- -Product Page
- -Main Shopping Page
- +Home Page
- -Incorporate the information from the Residential and Commercial pages on the original website
- -Seal or Banner that says Veteran Owned Business
- -Seal or Banner that shows we are eco-friendly
- -Testimonial section
Nice to have
- -Social media link s

```html
<!DOCTYPE html>
<html lang="en">
<head>
<meta charset="utf-8">
<title>Corvenly Postbox – Home</title>
<link rel="stylesheet" href="https://fonts.googleapis.com/css2?family=Playfair+Display:wght@400;700&family=Open+Sans:wght@400;600;700&display=swap">
<style>
:root{
  --marine:#04604c;
  --lime:#7cc242;
  --mint:#5bc08f;
  --slate:#9fa0ab;
  --ink:#333;
  --muted:#666;
  --line:#d9d9d9;
  --paper:#fff;
  --mist:#ececec;
  --foot:#efefef;
}
*{box-sizing:border-box;margin:0;padding:0}
html,body{width:1200px;height:3125px;overflow:hidden}
body{font-family:"Open Sans",sans-serif;color:var(--ink);background:var(--paper);position:relative}
.serif{font-family:"Playfair Display",serif}
.abs{position:absolute}
.wrap{position:absolute;left:173px;width:855px}

/* top bar */
.topbar{position:absolute;top:0;left:0;width:1200px;height:30px;border-bottom:1px solid #eee}
.topbar .social{position:absolute;left:173px;top:6px;display:flex;gap:4px}
.social span{width:18px;height:18px;border-radius:50%;background:#9a9a9a;display:block}
.topbar .call{position:absolute;left:0;width:1200px;top:5px;text-align:center;font-size:15px;letter-spacing:.3px;color:#444}
.topbar .sign{position:absolute;left:915px;top:0;height:30px;width:112px;border-left:1px solid #eee;border-right:1px solid #eee;font-size:11px;color:#666;text-align:center;line-height:30px}

/* nav */
.nav{position:absolute;top:30px;left:0;width:1200px;height:95px}
.brand{position:absolute;left:173px;top:36px;display:flex;align-items:center;gap:8px;font-size:17px;font-weight:700;color:var(--marine)}
.brand i{width:22px;height:22px;background:var(--lime);display:block}
.menu{position:absolute;right:173px;top:38px;display:flex;gap:26px;font-size:11px;color:#555;align-items:center;text-transform:uppercase;letter-spacing:.3px}

/* hero */
.hero{position:absolute;top:125px;left:0;width:1200px;height:485px;background:linear-gradient(180deg,#8fb6dc 0%,#a9c2d6 30%,#6f5a4a 55%,#5d4a3c 75%,#6f9a45 90%,#5d8a3a 100%)}
.badge{position:absolute;left:192px;top:240px;width:156px;height:50px;background:#1f3d7a;border-radius:6px}
.hero h1{position:absolute;left:190px;top:300px;font-size:46px;font-weight:400;color:#fff}
.hero p{position:absolute;left:198px;top:368px;width:360px;font-size:16px;line-height:22px;color:#fff}
.btn{display:inline-block;background:var(--mint);color:#fff;font-size:12px;font-weight:700;text-transform:uppercase;border-radius:5px;text-align:center}
.hero .btn{position:absolute;left:200px;top:483px;width:116px;height:34px;line-height:34px}

/* online band */
.online{position:absolute;top:610px;left:0;width:1200px;height:145px;background:var(--marine);color:#fff;text-align:center}
.online .l1{position:absolute;top:32px;width:100%;font-size:34px}
.online .l2{position:absolute;top:78px;width:100%;font-size:27px}

/* tiles */
.tiles{position:absolute;top:755px;left:0;width:1200px;height:272px;display:flex}
.tile{position:relative;flex:1;margin-right:2px}
.tile:last-child{margin-right:0}
.tile .ph{position:absolute;inset:0}
.tile .label{position:absolute;left:0;right:0;top:188px;height:46px;line-height:46px;text-align:center;color:#fff;font-size:33px}
.t1 .ph{background:linear-gradient(160deg,#b8a98f,#3a3a3a 60%,#7a7a62)}
.t2 .ph{background:linear-gradient(160deg,#cfd9c8,#4b4a3f 55%,#8a7c62)}
.t3 .ph{background:linear-gradient(160deg,#8d6a4a,#4f4036 55%,#9a8d82)}
.t1 .label{background:var(--lime)}
.t2 .label{background:var(--mint)}
.t3 .label{background:var(--slate)}

/* welcome */
.welcome{position:absolute;top:1027px;left:0;width:1200px;height:344px;text-align:center}
.welcome .pre{position:absolute;top:55px;width:100%;font-size:25px;letter-spacing:1px;color:#444}
.welcome h2{position:absolute;top:82px;width:100%;font-size:40px;font-weight:700;color:#222}
.welcome h2 em{font-style:normal;color:var(--lime)}
.rule{position:absolute;height:1px;background:var(--line)}
.welcome .text{position:absolute;left:173px;top:160px;width:855px;font-size:13px;line-height:21px;color:#555}
.welcome .text p{margin-bottom:10px}

/* testimonials */
.testi{position:absolute;top:1371px;left:0;width:1200px;height:406px;background:var(--slate);color:#fff}
.testi h3{position:absolute;top:45px;width:100%;text-align:center;font-size:30px;font-weight:400;color:#f3f3f3}
.avatar{position:absolute;left:246px;top:139px;width:208px;height:208px;border-radius:50%;background:linear-gradient(160deg,#d8d0c4,#b07a5a 55%,#5bb3a2);border:5px solid #fff}
.quote{position:absolute;left:483px;top:168px;width:460px;font-size:20px;line-height:28px}
.who{position:absolute;left:483px;top:256px;font-size:20px;font-weight:700}
.role{position:absolute;left:483px;top:284px;font-size:14px}
.arrow{position:absolute;top:221px;width:44px;height:44px;border-radius:50%;background:#fff}
.dots{position:absolute;top:344px;left:560px;display:flex;gap:5px}
.dots span{width:10px;height:10px;border-radius:50%;background:#c9cad0}
.dots span:first-child{background:#fff}

/* guarantee */
.guar{position:absolute;top:1777px;left:0;width:1200px;height:306px;background:var(--mist)}
.guar .ph{position:absolute;left:0;top:0;width:588px;height:306px;background:linear-gradient(140deg,#2c2c2c,#6b5a3e 45%,#2a2a2a 75%,#5a5a5a)}
.guar h3{position:absolute;left:610px;top:56px;font-size:24px;font-weight:400;color:#222}
.guar p{position:absolute;left:610px;top:100px;width:418px;font-size:13px;line-height:20.5px;color:#555}

/* blogs */
.blogs{position:absolute;top:2083px;left:0;width:1200px;height:448px;border-bottom:1px solid #eee}
.blogs h3{position:absolute;top:52px;width:100%;text-align:center;font-size:32px;font-weight:400;color:#222}
.card{position:absolute;top:127px;width:271px;height:309px}
.card .ph{position:absolute;inset:0}
.card h4{position:absolute;left:20px;top:20px;width:230px;font-size:17px;line-height:21px;font-weight:700;color:#fff}
.card .date{position:absolute;left:20px;bottom:16px;font-size:11px;color:#fff}
.c1{left:173px}.c1 .ph{background:linear-gradient(170deg,#6a5545,#4a4a4a 50%,#8a7060)}
.c2{left:465px;border:5px solid var(--mint)}.c2 .ph{background:linear-gradient(170deg,#8fb0d8,#8a7560 45%,#4d7a3a)}
.c3{left:756px}.c3 .ph{background:linear-gradient(170deg,#c7c9cc,#6e6258 55%,#9a8c7e)}

/* cta */
.cta{position:absolute;top:2589px;left:0;width:1200px;height:251px;background:var(--marine);color:#fff;text-align:center}
.cta p{position:absolute;top:68px;width:100%;font-size:32px;line-height:34px}
.cta .btn{position:absolute;left:438px;top:148px;width:324px;height:40px;line-height:40px;border-radius:20px;font-size:12px}

/* footer */
.footer{position:absolute;top:2840px;left:0;width:1200px;height:285px;background:var(--foot);font-size:11px;color:#555}
.col{position:absolute;top:34px}
.col h5{font-size:13px;font-weight:700;color:#333;text-transform:uppercase;padding-bottom:10px;border-bottom:1px solid var(--line);margin-bottom:12px}
.c-contact{left:173px;width:190px}
.c-links{left:392px;width:190px}
.c-follow{left:610px;width:190px}
.c-news{left:829px;width:198px}
.info{display:flex;gap:10px;margin-bottom:10px;line-height:15px}
.info svg{flex:none;margin-top:2px}
.links li{list-style:none;line-height:22px}
.links li::before{content:"›";margin-right:6px}
.fsocial{display:flex;gap:12px}
.fsocial span{width:22px;height:22px;border-radius:50%;background:#555;display:block}
.input{margin-top:10px;height:30px;border:1px solid #ddd;background:#fff;padding-left:8px;line-height:28px;font-size:10px;color:#888}
.sub{margin-top:8px;height:30px;line-height:30px;width:100%;border-radius:0;font-size:11px}
.bottom{position:absolute;left:173px;top:243px;width:855px;border-top:1px solid var(--line);text-align:center;padding-top:12px;font-size:12px;color:#555}
</style>
</head>
<body>

<header class="topbar">
  <div class="social" aria-label="Social links"><span></span><span></span><span></span><span></span><span></span></div>
  <div class="call">CALL NOW TO ORDER! (555)-318-2270</div>
  <div class="sign">Sign In/Register</div>
</header>

<nav class="nav">
  <div class="brand"><i></i>Corvenly Postbox</div>
  <div class="menu">
    <span>Home</span><span>About</span><span>Products</span><span>Commercial</span><span>Residential</span><span>Gallery</span><span>Contact Us</span>
    <svg width="18" height="18" viewBox="0 0 18 18"><circle cx="7.5" cy="7.5" r="5.5" fill="none" stroke="#333" stroke-width="2"/><line x1="11.5" y1="11.5" x2="16" y2="16" stroke="#333" stroke-width="2"/></svg>
    <svg width="18" height="18" viewBox="0 0 18 18"><path d="M1 2h3l2 9h9l2-7H5" fill="none" stroke="#333" stroke-width="1.6"/><circle cx="7" cy="15" r="1.5" fill="#333"/><circle cx="14" cy="15" r="1.5" fill="#333"/></svg>
  </div>
</nav>

<section class="hero" role="img" aria-label="Brick house with a dark pedestal mailbox on the front lawn">
</section>
<div class="badge" role="img" aria-label="Veteran owned business seal"></div>
<div class="hero" style="background:none">
  <h1 class="serif" style="top:175px">The Regent</h1>
  <p style="top:243px">Elegent in design. Impervious to the elements. Superior engineering. Excellence in manufacturing. Premium enamel finish, increased property value.</p>
  <span class="btn" style="top:358px">Shop Mailbox</span>
</div>

<section class="online serif">
  <div class="l1">Buy Mailboxes Online from</div>
  <div class="l2">Corvenly Postbox Company</div>
</section>

<section class="tiles">
  <div class="tile t1"><div class="ph" role="img" aria-label="Commercial cluster mailbox units"></div><div class="label serif">Commercial</div></div>
  <div class="tile t2"><div class="ph" role="img" aria-label="Residential mailbox in front of a house"></div><div class="label serif">Residential</div></div>
  <div class="tile t3"><div class="ph" role="img" aria-label="Craftsman welding a custom mailbox"></div><div class="label serif">Customize Your Own</div></div>
</section>

<section class="welcome">
  <div class="pre serif">WELCOME TO</div>
  <div class="rule" style="left:173px;top:118px;width:175px"></div>
  <div class="rule" style="left:852px;top:118px;width:176px"></div>
  <h2 class="serif">Corvenly <em>Postbox</em> Company</h2>
  <div class="text">
    <p>Corvenly Postbox Company offers postal products that are not only appealing, but also durable and add "Curb Appeal" to your home or development. Because quality is our reputation, we only offer a select number of manufacturer's products.</p>
    <p>Not only will you be rewarded with the highest quality mailbox, street sign, light post or garden accessory on the market, you will experience customer service like you've never seen before.</p>
    <p>We know you have many choices when it comes to postal specialties, as well as who to purchase from; we appreciate that you have chosen us.</p>
  </div>
</section>

<section class="testi">
  <h3 class="serif">What People Are Saying</h3>
  <div class="arrow" style="left:172px"><svg width="44" height="44" viewBox="0 0 44 44"><path d="M25 15l-7 7 7 7" fill="none" stroke="#888" stroke-width="3"/></svg></div>
  <div class="avatar" role="img" aria-label="Photo of a smiling customer couple"></div>
  <p class="quote">“I love my mailbox! Thank you for your quick response. Doing business with your company has always been a good experience!”</p>
  <div class="who">Marissa Dellwood</div>
  <div class="role">Homeowner</div>
  <div class="arrow" style="left:984px"><svg width="44" height="44" viewBox="0 0 44 44"><path d="M19 15l7 7-7 7" fill="none" stroke="#888" stroke-width="3"/></svg></div>
  <div class="dots"><span></span><span></span><span></span><span></span><span></span></div>
</section>

<section class="guar">
  <div class="ph" role="img" aria-label="Close-up of bronze and black decorative mailboxes"></div>
  <h3 class="serif">100% Satisfaction Guarantee</h3>
  <p>Lorem ipsum dolor sit amet, consectetur adipiscing elit, sed do eiusmod tempor incididunt ut labore et dolore magna aliqua. Ut enim ad minim veniam, quis nostrud exercitation ullamco laboris nisi ut aliquip ex ea commodo consequat. Duis aute irure dolor in reprehenderit in voluptate velit esse cillum dolore eu fugiat nulla pariatur. Excepteur sint occaecat cupidatat non proident, sunt in culpa qui officia deserunt mollit anim id est laborum.</p>
</section>

<section class="blogs">
  <div class="rule" style="left:173px;top:73px;width:300px"></div>
  <div class="rule" style="left:728px;top:73px;width:300px"></div>
  <h3 class="serif">Latest Blogs</h3>
  <article class="card c1"><div class="ph" role="img" aria-label="Black mailbox with house number on brick pillar"></div><h4>Lorem ipsum dolor sit amet, consectetur adipiscing elit</h4><div class="date">01 JAN, 2018</div></article>
  <article class="card c2"><div class="ph" role="img" aria-label="Stone mailbox column in front of a home"></div><h4>Lorem ipsum dolor sit amet, consectetur adipiscing elit</h4><div class="date">05 JAN, 2018</div></article>
  <article class="card c3"><div class="ph" role="img" aria-label="Post-mounted mailbox beside a yard sign"></div><h4>Lorem ipsum dolor sit amet, consectetur adipiscing elit</h4><div class="date">08 JAN, 2018</div></article>
</section>

<section class="cta">
  <p class="serif">Our goal is safety and security for your mail. Locking<br>mailboxes protect your mail, secure your life</p>
  <span class="btn">Shop Heavy Duty Security Mailboxes</span>
</section>

<footer class="footer">
  <div class="col c-contact">
    <h5>Contact Us</h5>
    <div class="info"><svg width="12" height="14" viewBox="0 0 12 14"><path d="M6 1a4.5 4.5 0 0 0-4.5 4.5C1.5 9 6 13 6 13s4.5-4 4.5-7.5A4.5 4.5 0 0 0 6 1z" fill="#555"/><circle cx="6" cy="5.5" r="1.6" fill="#efefef"/></svg><div>42 Linden Crest Rd<br>Maple Fork, Westara 40117</div></div>
    <div class="info"><svg width="12" height="14" viewBox="0 0 12 14"><path d="M2 1l3 1 1 3-2 1a7 7 0 0 0 3 3l1-2 3 1 0 3c-5 0-9-4-9-10z" fill="#555"/></svg><div>Phone<br>(555)-318-2270</div></div>
    <div class="info"><svg width="12" height="14" viewBox="0 0 12 14"><rect x="1" y="3" width="10" height="8" fill="#555"/><rect x="3" y="1" width="6" height="3" fill="#555"/></svg><div>Fax<br>(555)-318-2270</div></div>
    <div class="info"><svg width="12" height="14" viewBox="0 0 12 14"><rect x="0.5" y="3" width="11" height="8" fill="none" stroke="#555"/><path d="M1 3.5l5 4 5-4" fill="none" stroke="#555"/></svg><div>Email<br>info@corvenlypostbox.example</div></div>
  </div>
  <div class="col c-links">
    <h5>Quick Links</h5>
    <ul class="links"><li>Home</li><li>About</li><li>Products</li><li>Commercial</li><li>Residential</li><li>Gallery</li><li>Contact Us</li></ul>
  </div>
  <div class="col c-follow">
    <h5>Follow Us</h5>
    <div class="fsocial" aria-label="Social links"><span></span><span></span><span></span><span></span><span></span></div>
  </div>
  <div class="col c-news">
    <h5>Subscribe Newsletter</h5>
    <div style="line-height:15px">Join the Corvenly Postbox for regular updates and information.</div>
    <div class="input">Enter your email address</div>
    <div class="btn sub">Subscribe</div>
  </div>
  <div class="bottom">© 2018 Corvenly Postbox Co. All Rights Reserved. &nbsp;|&nbsp; Terms of Use &nbsp;|&nbsp; Privacy Policy</div>
</footer>

</body>
</html>
```